Food Label Packaging Design Remake Redesign

We are ready for a redo! We want to remake our food label to be more fun, beachy and modern to better reflect our brand's desired vibe and the actual meaning of ‘zingabop’ as a boisterous party, noisy excitement.

Please first reference the current label and logo elements attached. You can also reference our website www.zingabopgrill.com. We want to give our current look the refreshed look described above.

The remaining images represent a design board of interest and inspiration for new color combinations, font style, background, cowgirl meets beach and surf!

REQUIRED elements are
1) The full company name: ZINGABOP GRILL spelled like this and all caps.
2) The cowgirl - she can be modified to include the surfboard somehow to make her a beachy cowgirl/maybe surfer girl - but she cannot be in a bikini she needs to still have pants/boots on...as in a 'mash up' of cowgirl and beach/surfer girl that represents the noisy excitement of a 'zingabop' . Please do NOT cut her in half
3) The ‘Tucked with a Wink’ seal to have that matches to have a beachy, playful feel to it, maybe palm tree/kiss lips combo ?
4) Much of the right side of the label must be included but can be presented in a totally different way: the preparation directions, the nutritional panel nd bottom right product information. all can be rearranged - its most important that the preparation instructions are legible.
5) Product title

**Please DO NOT make country-western**

Target Market(s)

Moms, Dads and Singles who are 'foodies' with a busy family and social, work schedule who value authentic, great tasting food that is authentic, boutique and better than for you, convenient, and fun to feed and entertain their friends and families.

Industry/Entity Type

food - CPG Consumer Packaged Foods

Font styles to use
Other font styles liked:
• Cursive, playful andf fun! PLEASE SEE FONT IDEAS IN IMAGES ATTACHED

Colors
0094D4
00A9DD
6FCCEA
C7EBF8
E9F6FB
00AB8E
00BBA5
67D7C9
C6EFE9
E9F9F6
FFC000
F8CF3A
FAE287
FDF2CF
FEFAEE
F0912C
F2A743
F7CA91
FBE8D2
FDF5EE
E54698
E96AAD
F1A4CE
F9D9EA
FCEFF6

Requirements
Must have
• Please see above. Colors: I would like to maintain pink as the main color, along with a cool new beachy black/gray. The other colors below are of interest and are also represented in image ideas provided. Logo - take out 'Marlena's Grill' and include the phonetic description of zingabop near/a part of logo zingabop: /zing a bop/ Ingredients and Nutrtional panel - content doesn't have to be exact but must be represented to scale, but may be decreased in size, especially the nutrition panel. Please be sure the preparation instructions are legible, not too small.
Nice to have
• PLEASE SEE THE NEW INFO GRAPHIC with the 'sun' to consider and also the fun, cursive font to consider in your design. thank you!
Should not have
• Please see above!

```html
<!DOCTYPE html>
<html lang="en">
<head>
<meta charset="utf-8">
<title>Zingabop Grill – Smoked Chopped Beef Brisket Label</title>
<link rel="stylesheet" href="https://fonts.googleapis.com/css2?family=Oswald:wght@400;500;600&family=Roboto+Condensed:wght@400;700&family=Arimo:wght@400;700&display=swap">
<style>
  :root {
    --orange: #F8A54C;
    --pink: #E54698;
    --pink-mid: #E96AAD;
    --pink-soft: #ECA3CB;
    --ink: #231F20;
    --rule: #555555;
    --grey-bg: #D6D6D6;
    --white: #FFFFFF;
  }
  * { box-sizing: border-box; margin: 0; padding: 0; }
  html, body { width: 938px; height: 1200px; overflow: hidden; background: var(--white); }
  .canvas { position: relative; width: 938px; height: 1200px; font-family: "Roboto Condensed", sans-serif; color: var(--ink); }

  /* Brand panel */
  .brand-panel { position: absolute; left: 7px; top: 8px; width: 922px; height: 542px; background: var(--orange); }
  .brand-dot { position: absolute; left: 444px; top: 150px; width: 34px; height: 34px; border-radius: 50%; background: var(--pink); }
  .brand-tag { position: absolute; left: 280px; right: 280px; top: 250px; display: flex; align-items: center; gap: 10px; }
  .brand-tag::before, .brand-tag::after { content: ""; flex: 1; height: 2px; background: var(--rule); }
  .brand-tag span { font-family: "Oswald", sans-serif; font-weight: 600; font-size: 22px; line-height: 1; letter-spacing: 2px; color: var(--pink); }
  .brand-name { position: absolute; left: 0; right: 0; top: 272px; text-align: center; font-family: "Oswald", sans-serif; font-weight: 600; font-size: 86px; line-height: 1; letter-spacing: 4px; color: var(--pink); }
  .brand-phonetic { position: absolute; left: 0; right: 0; top: 366px; text-align: center; font-family: "Arimo", sans-serif; font-size: 27px; color: #3a3a3a; letter-spacing: 1px; }

  /* Pouch stage */
  .pouch-stage { position: absolute; left: 0; top: 557px; width: 938px; height: 643px; background: var(--grey-bg); }
  .label { position: absolute; left: 177px; top: 134px; width: 596px; height: 368px; background: var(--white); }

  /* Front panel */
  .label-front { position: absolute; left: 0; top: 0; width: 323px; height: 368px; background: var(--pink-mid); }
  .label-front-inner { position: absolute; left: 11px; top: 11px; right: 11px; bottom: 11px; background: var(--pink-soft); }
  .front-tag { position: absolute; left: 60px; right: 60px; top: 82px; display: flex; align-items: center; gap: 5px; }
  .front-tag::before, .front-tag::after { content: ""; flex: 1; height: 1px; background: var(--rule); }
  .front-tag span { font-family: "Oswald", sans-serif; font-weight: 600; font-size: 9px; line-height: 1; letter-spacing: 1px; color: var(--pink); }
  .front-name { position: absolute; left: 0; right: 0; top: 92px; text-align: center; font-family: "Oswald", sans-serif; font-weight: 600; font-size: 32px; line-height: 1; letter-spacing: 2px; color: var(--pink); }
  .front-phonetic { position: absolute; left: 0; right: 0; top: 131px; text-align: center; font-family: "Arimo", sans-serif; font-size: 11px; color: #3a3a3a; }
  .product-title { position: absolute; left: 27px; top: 180px; font-family: "Oswald", sans-serif; font-weight: 600; font-size: 31px; line-height: 37.5px; text-transform: uppercase; color: var(--white); }
  .product-title .accent { color: var(--pink); }
  .wink-seal { position: absolute; left: 179px; top: 225px; width: 92px; height: 92px; border-radius: 50%; background: var(--pink); border: 3px solid var(--white); }

  /* Directions */
  .directions { position: absolute; left: 343px; top: 17px; width: 86px; font-size: 7.6px; line-height: 10.6px; }
  .directions .tagline { color: var(--pink); font-weight: 700; margin-bottom: 12px; }
  .directions h4 { font-size: 7.6px; font-weight: 700; }
  .directions p { margin-bottom: 10px; }
  .ingredients { font-weight: 700; text-transform: uppercase; font-size: 6.6px; line-height: 10.6px; }

  /* Nutrition */
  .nutrition { position: absolute; left: 442px; top: 20px; width: 128px; height: 252px; background: var(--ink); border-radius: 4px; padding: 3px; font-family: "Arimo", sans-serif; }
  .nutrition-card { background: var(--white); border-radius: 3px; height: 198px; padding: 4px 4px; font-size: 5.4px; line-height: 8.6px; }
  .nutrition-card h3 { font-size: 14px; line-height: 15px; font-weight: 700; }
  .nf-sub { line-height: 7px; }
  .nf-row { display: flex; justify-content: space-between; border-top: 0.5px solid var(--ink); }
  .nf-row.thick { border-top: 3px solid var(--ink); }
  .nf-row.indent span:first-child { padding-left: 6px; }
  .nf-note { border-top: 3px solid var(--ink); padding-top: 2px; font-size: 5.2px; line-height: 6.2px; }
  .distributor { position: absolute; left: 8px; top: 208px; width: 60px; color: var(--white); font-family: "Roboto Condensed", sans-serif; font-size: 4.6px; line-height: 6.5px; font-weight: 700; }
  .inspection-mark { position: absolute; left: 78px; top: 206px; width: 38px; height: 38px; border-radius: 50%; background: var(--white); }

  /* Product info */
  .product-info { position: absolute; right: 24px; top: 309px; text-align: right; font-size: 6.4px; line-height: 8px; font-weight: 700; text-transform: uppercase; }
  .product-info .social { color: var(--pink); font-weight: 400; }
  .product-info .spacer { height: 6px; }
</style>
</head>
<body>
<div class="canvas">

  <section class="brand-panel">
    <span class="brand-dot"></span>
    <div class="brand-tag"><span>GRILL</span></div>
    <h1 class="brand-name">ZINGABOP</h1>
    <p class="brand-phonetic">/zing • a • bop/</p>
  </section>

  <section class="pouch-stage">
    <article class="label">
      <div class="label-front">
        <div class="label-front-inner">
          <div class="front-tag"><span>GRILL</span></div>
          <h2 class="front-name">ZINGABOP</h2>
          <p class="front-phonetic">/zing • a • bop/</p>
          <h3 class="product-title">Smoked<br><span class="accent">Chopped</span><br>Beef<br>Brisket</h3>
          <div class="wink-seal" role="img" aria-label="Tucked with a Wink seal"></div>
        </div>
      </div>

      <div class="directions">
        <p class="tagline">FULLY COOKED!<br>JUST HEAT, SERVE,<br>AND ENJOY!</p>
        <h4>REHEAT INSTRUCTIONS;</h4>
        <p><strong>OVEN;</strong> Our FAVORITE Way! Preheat oven to 250 F, Remove meat from pouch, Place in oven safe dish, Cover and reheat for 10-12 Minutes per each pound to Temperature</p>
        <p><strong>MICROWAVE:</strong> Remove Meat from pouch, place in Microwave safe dish. Follow Microwave instructions to Reheat to temperature. (Approximately 45 seconds To 1.5 minutes per each Pound, stirring Occasionally.)</p>
        <p class="ingredients">Ingredients: Choice beef brisket, Zingabop BBQ rub (blend of salt, spices, sugar, garlic powder, paprika, onion powder, native food starch, turmeric, natural hickory smoke flavor, extractive of paprika, extractive of spice.)</p>
      </div>

      <div class="nutrition">
        <div class="nutrition-card">
          <h3>Nutrition Facts</h3>
          <div class="nf-sub">Serving Size oz.</div>
          <div class="nf-sub">Serving Per Container</div>
          <div class="nf-row thick"><span>Amount Per Serving:</span></div>
          <div class="nf-row"><span>Calories</span><span>Calories From Fat</span></div>
          <div class="nf-row thick"><span></span><span>% Daily value*</span></div>
          <div class="nf-row"><span>Total Fat</span><span>%</span></div>
          <div class="nf-row indent"><span>Saturated Fat</span><span>%</span></div>
          <div class="nf-row indent"><span>Trans Fat</span><span></span></div>
          <div class="nf-row"><span>Cholesterol</span><span>%</span></div>
          <div class="nf-row"><span>Sodium</span><span>%</span></div>
          <div class="nf-row"><span>Total Carbohydrate</span><span>%</span></div>
          <div class="nf-row indent"><span>Dietary Fiber</span><span>%</span></div>
          <div class="nf-row indent"><span>Sugars</span><span></span></div>
          <div class="nf-row"><span>Protein</span><span></span></div>
          <p class="nf-note">*Percent Daily values are based on a 2000 calorie diet. Your daily values may be higher or lower depending on you calorie needs.</p>
        </div>
        <p class="distributor">DISTRIBUTED BY:<br>ZINGABOP GRILL<br>118 Seabreeze Lane<br>Harbor Point,<br>VA 20000</p>
        <div class="inspection-mark" role="img" aria-label="Inspection mark"></div>
      </div>

      <div class="product-info">
        <p class="social">#ZINGABOPLIVIN</p>
        <p class="social">www.zingabopgrill.com</p>
        <div class="spacer"></div>
        <p>Keep frozen / refrigerated</p>
        <p>Net wt. 16oz (1lb)</p>
      </div>
    </article>
  </section>

</div>
</body>
</html>
```